New homepage concept needed for online reading programs website

About the Academy of Literacy Growth:
The Institute teaches online summer reading skills programs for entering fourth graders, offered through partnerships with universities, colleges, and municipalities nationwide. The goal of the program is to build reading skills (long-word decoding, fluency and comprehension), and foster a lifelong love of books and reading.

Aims & Target Market:
The Institute has developed a new format of its online reading program for fourth graders, which includes live small-group video classes taught by a professional reading teacher. The Institute seeks a mock-up of a homepage of the website used to market this new program. The primary audience for this website is the parents of these 4th graders. Traffic to this website is driven by direct-marketing campaigns directed at parents and students.

Live classes for children are completely new in online education, unlike anything else in the marketplace, and parents therefor have no experience with them. The successful homepage mock-up will include illustrations or photographs that allow visitors to immediately grasp/understand the new format, without relying on a written description. Additionally, the successful homepage concept will make the program, and the video classes in particular, feel fun and appealing to kids and parents alike.

There are three main elements to the program, and each needs to be represented graphically on the homepage, with particular emphasis on the small-group video classes:
1. Live small-group video classes (weekly for six weeks):
a. During video class discussions, the student’s computer (or tablet) screen is filled with live video frames of the teacher and the other students. The video frame for the teacher is larger, and the other students appear in smaller frames.
b. During other video class instruction, the teacher uses a presentation screen to display pages of a book or a “whiteboard” used for instructional activities.
c. The homepage mock-up could include a screenshot of the video classes themselves, with children looking engaged and a teacher leading them in discussion. We have included a screen shot of one of these classes for reference, but do not feel constrained to represent this screen realistically (as shown here). It can be changed around – teacher in the center, etc.). Alternately, if there is a graphic other than a screen shot that you feel could be used to bring across the concept of the video classes, feel free.
2. Individualized online instruction
a. Graphics could include screenshots of the video lessons students complete in between these weekly classes and/or images of a child or children at computer(s).
3. Independent reading in great books
a. Graphics could include some or all of the program books, which can be pulled from our current website (link below), and/or images of a child or children reading.

An example of our current online program website can be seen at http://fenwick.webliteracystudio.example/4/Home. Please reference this site for information on program goals, books/materials, and site navigation.
The successful design will be welcoming and inviting, and allow parents and students to immediately grasp what the programs are, with particular emphasis on the live small-group video classes.

Copy and Specifications:
Sample copy has been provided for reference, as well as a screen shot of our sample classes to show what students will see on screen. Also included are stills of our online video lessons to illustrate the online instruction aspect.

```html
<!DOCTYPE html>
<html lang="en">
<head>
<meta charset="utf-8">
<title>Reading Skills – Online Program for 4th and 5th Graders</title>
<link href="https://fonts.googleapis.com/css2?family=Open+Sans:wght@400;600;700&family=Nunito:wght@800&display=swap" rel="stylesheet">
<style>
:root{
  --header:#0b2418;
  --gold-1:#ffd84d;
  --gold-2:#f7b71d;
  --nav-ink:#3a2f10;
  --hero:#1f6ec6;
  --hero-head:#f7d448;
  --card:#f0f0f0;
  --ink:#333;
  --link:#1c63b7;
  --footer:#1b1b1b;
  --footer-text:#d6d6d6;
  --orange:#f26a1b;
  --sky:#6ab6ee;
}
*{box-sizing:border-box;margin:0;padding:0}
html,body{width:834px;height:1200px;overflow:hidden}
body{position:relative;font-family:"Open Sans",Arial,sans-serif;background:#fff;color:var(--ink)}
.abs{position:absolute}

.site-header{left:0;top:0;width:834px;height:67px;background:var(--header);border-top:6px solid #000}
.site-title{left:82px;top:2px;font-family:"Nunito","Open Sans",sans-serif;font-weight:800;font-size:31px;color:#3fae5a;letter-spacing:.2px}
.site-tagline{left:81px;top:44px;font-size:12px;font-weight:700;color:#f3a521}
.search{left:572px;top:16px;width:161px;height:27px;background:#fff;border-radius:2px;display:flex;align-items:center;padding-left:8px;font-size:7.5px;color:#555}
.search svg{margin-right:8px}

.nav-list{list-style:none;display:flex;font-size:10.5px}
.nav-list li{margin-right:22.5px}
.main-nav{left:0;top:67px;width:834px;height:38px;background:linear-gradient(var(--gold-1),var(--gold-2))}
.main-nav .nav-list{position:absolute;left:82px;top:12px;color:var(--nav-ink)}

.hero{left:0;top:105px;width:834px;height:291px;background:var(--hero)}
.hero-lead{left:106px;top:44px;width:330px;font-size:13px;line-height:15px;color:var(--hero-head)}
.hero-points{left:108px;top:101px;list-style:none;color:#fff;font-size:10px;line-height:16.8px}
.hero-points li{position:relative;padding-left:14px}
.hero-points li::before{content:"";position:absolute;left:1px;top:7px;width:4px;height:4px;background:#fff;transform:rotate(45deg)}
.hero-body{left:106px;top:178px;width:300px;font-size:10px;line-height:12.5px;color:#fff}
.btn{display:flex;align-items:center;justify-content:center;border-radius:3px;color:#fff;font-size:13px}
.btn-book{left:106px;top:236px;width:140px;height:31px;background:linear-gradient(#8fcaf5,var(--sky));letter-spacing:.3px}
.btn-video{left:250px;top:236px;width:195px;height:31px;background:linear-gradient(#ff8a33,var(--orange))}
.hero-media{left:453px;top:39px;width:268px;height:227px;border-radius:6px;background:linear-gradient(#5ba2e0,#2f7ccc 70%,#d9dde2 72%,#eef0f2)}
.arrow{top:119px;width:38px;height:38px;background:#17508f;display:flex;align-items:center;justify-content:center}
.arrow-prev{left:0;border-radius:0 3px 3px 0}
.arrow-next{left:796px;border-radius:3px 0 0 3px}

.site-footer{left:0;top:910px;width:834px;height:290px;background:var(--footer)}

.feature{top:405px;width:217px;height:544px;background:var(--card)}
.feature-1{left:83px}.feature-2{left:308px}.feature-3{left:531px}
.feature-icon{position:absolute;left:13px;top:14px;width:31px;height:31px;border-radius:50%;display:flex;align-items:center;justify-content:center}
.feature-title{position:absolute;left:52px;top:16px;font-size:13px;line-height:15.5px;color:#222;font-weight:400}
.feature-sub{position:absolute;left:52px;top:48px;font-size:9px;color:#333}
.feature-media{position:absolute;left:14px;top:74px;width:189px;height:116px}
.feature-text{position:absolute;top:207px;width:195px}
.feature-notes{list-style:none;font-size:8.8px;line-height:15.2px;color:#333}
.feature-notes li{position:relative;padding-left:17px;margin-bottom:15.2px}
.feature-notes li:last-child{margin-bottom:0}
.feature-notes li::before{content:"";position:absolute;left:2px;top:5px;width:4px;height:4px;background:#333;transform:rotate(45deg)}
.read-more{display:block;margin:8px 0 0 17px;font-size:9px;color:var(--link);font-weight:600}
.caption{position:absolute;left:14px;top:178px;width:189px;height:12px;background:#fff;font-size:6.4px;color:#111;padding-left:16px;line-height:12px}

.partner{left:586px;top:966px;width:159px;height:21px;background:#17391f;display:flex;align-items:center;padding-left:6px;gap:6px;color:#f2d247;font-size:10.5px;letter-spacing:.6px}
.partner i{width:9px;height:11px;background:#f2d247;display:block}
.footer-nav{left:72px;top:999px}
.footer-nav .nav-list{color:var(--footer-text)}
.rule{left:0;width:834px;height:1px;background:#333}
.footer-head{font-size:13px;color:#ddd;font-weight:400}
.social{top:1092px;width:28px;height:28px}
.news-input{left:282px;top:1092px;width:139px;height:27px;background:#3b3b3b;color:#777;font-size:9.5px;padding:7px 12px}
.news-btn{left:421px;top:1092px;width:85px;height:27px;background:#2f7bc6;color:#fff;font-size:11px;display:flex;align-items:center;justify-content:center}
.contact{right:99px;top:1087px;text-align:right;color:#9a9a9a;font-size:9.5px;line-height:12px}
.copyright{left:0;width:834px;top:1170px;text-align:center;color:#8a8a8a;font-size:9.5px}
</style>
</head>
<body>

<header class="abs site-header">
  <div class="abs site-title">Reading Skills</div>
  <div class="abs site-tagline">Online Program for 4th and 5th Graders</div>
  <div class="abs search">
    <svg width="14" height="14" viewBox="0 0 14 14"><circle cx="5.5" cy="5.5" r="4.3" fill="none" stroke="#333" stroke-width="1.3"/><line x1="8.6" y1="8.6" x2="13" y2="13" stroke="#333" stroke-width="1.5"/></svg>
    What you are looking for ...
  </div>
</header>

<nav class="abs main-nav">
  <ul class="nav-list">
    <li>Home</li><li>Independent Reading</li><li>Comprehension</li><li>Long-Word Decoding</li><li>Fluency &amp; Speed</li><li>About the Teachers</li><li>FAQ</li><li>Enroll</li>
  </ul>
</nav>

<section class="abs hero">
  <p class="abs hero-lead">This program will help your child become a skilled, enthusiastic reader with strong comprehension. Your child will:</p>
  <ul class="abs hero-points">
    <li>Build long-word decoding skills</li>
    <li>Read more fluently and rapidly</li>
    <li>Improve comprehension</li>
    <li>Become a strong, enthusiastic reader</li>
  </ul>
  <p class="abs hero-body">The program includes engaging online instruction, effective materials, and great books, and is customized for your child’s reading level. You will also receive support from a professional reading teacher.</p>
  <div class="abs btn btn-book">BOOK NOW ONLINE</div>
  <div class="abs btn btn-video">Watch a Video Introduction</div>
  <div class="abs hero-media" role="img" aria-label="Desktop monitor showing a reading teacher holding a book beside an online lesson page"></div>
  <div class="abs arrow arrow-prev"><svg width="14" height="20" viewBox="0 0 14 20"><polyline points="11,2 3,10 11,18" fill="none" stroke="#fff" stroke-width="3"/></svg></div>
  <div class="abs arrow arrow-next"><svg width="14" height="20" viewBox="0 0 14 20"><polyline points="3,2 11,10 3,18" fill="none" stroke="#fff" stroke-width="3"/></svg></div>
</section>

<footer class="abs site-footer"></footer>

<article class="abs feature feature-1">
  <div class="feature-icon" style="background:#d9262e">
    <svg width="16" height="12" viewBox="0 0 16 12"><rect x="0" y="1" width="10" height="10" rx="1.5" fill="#fff"/><polygon points="10,6 16,1 16,11" fill="#fff"/></svg>
  </div>
  <h2 class="feature-title">Live small-group video classes</h2>
  <p class="feature-sub">weekly for six weeks</p>
  <div class="feature-media" role="img" aria-label="Screenshot of a live video class with the teacher in a large frame and students in small frames below" style="background:linear-gradient(#1c2b3e,#0a1320)"></div>
  <div class="feature-text" style="left:14px">
    <ul class="feature-notes">
      <li>During video class discussions, the student’s computer (or tablet) screen is filled with live video frames of the teacher and the other students. The video frame for the teacher is larger, and the other students appear in smaller frames.</li>
      <li>During other video class instruction, the teacher uses a presentation screen to display pages of a book or a “whiteboard” used for instructional activities.</li>
      <li>The homepage mock-up could include a screenshot of the video classes them-selves, with children looking engaged and a teacher leading them in discussion. We have included a screen shot of one of these classes for reference, but do not feel constrained to represent this screen realistically (as shown here)...</li>
    </ul>
    <span class="read-more">Read more ...</span>
  </div>
</article>

<article class="abs feature feature-2">
  <div class="feature-icon" style="background:#7b3fa0">
    <svg width="15" height="15" viewBox="0 0 15 15"><rect x="1" y="3" width="10" height="10" fill="none" stroke="#fff" stroke-width="1.4"/><line x1="5" y1="9" x2="13" y2="1" stroke="#fff" stroke-width="2"/></svg>
  </div>
  <h2 class="feature-title">Individualized online instruction</h2>
  <div class="feature-media" role="img" aria-label="Still from an online video lesson with a teacher presenting a vocabulary word on a blue background" style="background:linear-gradient(#2d8ae0,#2f79c9 88%,#f07a1e 92%)"></div>
  <div class="feature-text" style="left:13px">
    <ul class="feature-notes">
      <li>Graphics could include screenshots of the video lessons students complete in between these weekly classes and/or images of a child or children at computer(s).</li>
    </ul>
    <span class="read-more">Read more ...</span>
  </div>
</article>

<article class="abs feature feature-3">
  <div class="feature-icon" style="background:#1f8fd6">
    <svg width="16" height="13" viewBox="0 0 16 13"><path d="M1 2 Q4 0.5 8 2 Q12 0.5 15 2 V12 Q12 10.5 8 12 Q4 10.5 1 12 Z" fill="none" stroke="#fff" stroke-width="1.4"/><line x1="8" y1="2" x2="8" y2="12" stroke="#fff" stroke-width="1.4"/></svg>
  </div>
  <h2 class="feature-title" style="left:55px;top:18px">Independent reading in great books</h2>
  <div class="feature-media" role="img" aria-label="Video clip of two hosts reading books on a studio set" style="background:linear-gradient(#3b3f8e,#5a4a8a 60%,#7a4a3a)"></div>
  <div class="caption">Watch a clip from a <i>Story Circle News</i> episode.</div>
  <div class="feature-text" style="left:18px">
    <ul class="feature-notes">
      <li>Graphics could include some or all of the program books, which can be pulled from our current website (link below), and/or images of a child or children reading.</li>
    </ul>
    <span class="read-more">Read more ...</span>
  </div>
</article>

<div class="abs partner"><i></i>FENWICK</div>
<nav class="abs footer-nav">
  <ul class="nav-list">
    <li>Home</li><li>Independent Reading</li><li>Comprehension</li><li>Long-Word Decoding</li><li>Fluency &amp; Speed</li><li>About the Teachers</li><li>FAQ</li><li>Enroll</li>
  </ul>
</nav>
<div class="abs rule" style="top:1040px"></div>

<h3 class="abs footer-head" style="left:72px;top:1061px">Follow Us</h3>
<div class="abs social" style="left:72px;background:#3b5b9a" aria-label="Social link"></div>
<div class="abs social" style="left:106px;background:#2aa3e0" aria-label="Social link"></div>
<div class="abs social" style="left:141px;background:#d2403a" aria-label="Social link"></div>

<h3 class="abs footer-head" style="left:282px;top:1063px">News letter</h3>
<div class="abs news-input">Enter your email</div>
<div class="abs news-btn">Subscribe</div>

<h3 class="abs footer-head" style="right:100px;top:1061px">Contact Us</h3>
<div class="abs contact">Address<br>New Street<br>ph :xxxxx-xxx-xxx</div>

<div class="abs rule" style="top:1150px"></div>
<p class="abs copyright">Fenwick © 2014 Allright Reserved</p>

</body>
</html>
```